lunch and dinne(al a carte) menus

we are a medium sized licenced club that has taken back the dining in the club
in the western suburbs of sydney working class with a rugby league base
our logo is a wolf penbury hawks

Reason: We have changed the name to 77-13 diner it could be done as seventy 13 or 77 thirteen or seventy thirteen We need a lunch menu and a seperate dinner menu eg seventy 13 diner l u n c h or 77 thirteen diner d i n n e r

Reason: Weve changed the name

Target Market(s)

young families, working class rugby leagues sporty types

Industry/Entity Type

Club

Requirements
Must have
• user friendly

```html
<!DOCTYPE html>
<html lang="en">
<head>
<meta charset="utf-8">
<title>Dampers &amp; Light Meals Menu</title>
<link rel="stylesheet" href="https://fonts.googleapis.com/css2?family=Ultra&family=Tinos:ital,wght@1,700&display=swap">
<style>
  :root {
    --page: #ffffff;
    --field: #07941f;
    --field-line: #3fa84f;
    --ink: #0b0b0b;
  }
  html, body {
    margin: 0;
    padding: 0;
    width: 1000px;
    height: 1200px;
    overflow: hidden;
    background: var(--page);
  }
  .menu {
    display: block;
    width: 1000px;
    height: 1200px;
  }
  .menu__field { fill: var(--field); }
  .menu__line { fill: var(--field-line); }
  .section-title {
    font-family: "Ultra", "Rockwell", serif;
    fill: var(--ink);
  }
  .col-head,
  .item,
  .item-note,
  .price {
    font-family: "Tinos", "Times New Roman", serif;
    font-style: italic;
    font-weight: 700;
    fill: var(--ink);
  }
  .col-head { font-size: 15px; }
  .item { font-size: 15.5px; }
  .item-note { font-size: 15px; }
  .price { font-size: 15.5px; }
</style>
</head>
<body>
<svg class="menu" viewBox="0 0 1000 1200" xmlns="http://www.w3.org/2000/svg" aria-labelledby="menu-title">
  <title id="menu-title">Dampers and Light Meals menu</title>

  <!-- field background -->
  <rect class="menu__field" x="109" y="0" width="778" height="1200"/>

  <!-- field lines: horizontal -->
  <g class="field-lines">
    <rect class="menu__line" x="109" y="40" width="776" height="16"/>
    <rect class="menu__line" x="109" y="132" width="776" height="18"/>
    <rect class="menu__line" x="109" y="221" width="776" height="17"/>
    <rect class="menu__line" x="109" y="313" width="776" height="18"/>
    <rect class="menu__line" x="109" y="406" width="776" height="18"/>
    <rect class="menu__line" x="109" y="497" width="776" height="18"/>
    <rect class="menu__line" x="109" y="589" width="776" height="18"/>
    <rect class="menu__line" x="109" y="682" width="776" height="18"/>
    <rect class="menu__line" x="109" y="773" width="776" height="18"/>
    <rect class="menu__line" x="109" y="864" width="776" height="18"/>
    <rect class="menu__line" x="109" y="956" width="776" height="18"/>
    <rect class="menu__line" x="109" y="1048" width="776" height="18"/>
    <rect class="menu__line" x="109" y="1140" width="776" height="18"/>
    <!-- field lines: vertical -->
    <rect class="menu__line" x="140" y="40" width="23" height="1100"/>
    <rect class="menu__line" x="829" y="40" width="23" height="1100"/>
  </g>

  <!-- Dampers -->
  <text class="section-title" x="142" y="78" font-size="50">Dampers</text>
  <text class="col-head" x="681" y="69">Member</text>
  <text class="col-head" x="784" y="69">Visitor</text>

  <g class="section section--dampers">
    <text class="item" x="145" y="147">GARLIC DAMPER</text>
    <text class="price" x="694" y="147">$7</text><text class="price" x="773" y="147">$7</text>

    <text class="item" x="145" y="203">HERB DAMPER</text>
    <text class="price" x="694" y="203">$7</text><text class="price" x="773" y="203">$7</text>

    <text class="item" x="145" y="260">GARLIC &amp; CHEESE DAMPER</text>
    <text class="price" x="697" y="260">$7</text><text class="price" x="773" y="260">$7</text>

    <text class="item" x="145" y="317">BRUSCHETTA</text>
    <text class="price" x="696" y="317">$9</text><text class="price" x="772" y="317">$9</text>
  </g>

  <!-- Light Meals -->
  <text class="section-title" x="142" y="414" font-size="52">Light Meals</text>

  <g class="section section--light-meals">
    <text class="item" x="145" y="488">CHIPS</text>
    <text class="price" x="697" y="488">$6</text><text class="price" x="773" y="488">$6</text>

    <text class="item" x="145" y="544">WEDGES</text>
    <text class="item-note" x="145" y="573">With sour cream &amp; sweet chilli sauce</text>
    <text class="price" x="697" y="544">$6</text><text class="price" x="773" y="544">$6</text>

    <text class="item" x="145" y="630">BOWL OF SALAD</text>
    <text class="price" x="695" y="630">$6</text><text class="price" x="774" y="630">$6</text>

    <text class="item" x="145" y="687">BOWL OF STEAMED VEGETABES</text>
    <text class="price" x="698" y="687">$6</text><text class="price" x="773" y="687">$6</text>

    <text class="item" x="145" y="743">TEMPURA CRUMBED CALAMARI</text>
    <text class="item-note" x="145" y="772">Served with salad</text>
    <text class="price" x="695" y="743">$8</text><text class="price" x="774" y="743">$10</text>

    <text class="item" x="145" y="829">BATTERED FLATHEAD FILLETS</text>
    <text class="item-note" x="145" y="857">Served with salad</text>
    <text class="price" x="695" y="829">$8</text><text class="price" x="774" y="829">$10</text>

    <text class="item" x="145" y="914">WHITING FILLETS</text>
    <text class="item-note" x="145" y="942">Served with salad</text>
    <text class="price" x="693" y="914">$8</text><text class="price" x="772" y="914">$10</text>

    <text class="item" x="145" y="999">PRAWN SALAD</text>
    <text class="price" x="684" y="999">$10</text><text class="price" x="774" y="999">$12</text>

    <text class="item" x="145" y="1056">GARLIC OR CHILLI PRAWNS</text>
    <text class="item-note" x="145" y="1084">Served with rice &amp;salad</text>
    <text class="price" x="697" y="1056">$8</text><text class="price" x="775" y="1056">$10</text>
  </g>
</svg>
</body>
</html>
```